Business Card Design Project

Basic business card with minimal details. I just need company name, email & web address, telephone and my name.
I would like the back of the card to be grey with my logo & company name centred.

Target Market(s)

Architects
Builders
Property Developers

Industry/Entity Type

Business

Font styles to use
Sans Serif

Colors

Designer to choose colors to be used in the design.

Requirements
Must have
• Framewise Build
Marcus Helby - Director
M: 0427 593184
E: marcus@framewisebuild.com.au
W: www.framewisebuild.com.au
Should not have
• No other images or pictures

```html
<!DOCTYPE html>
<html lang="en">
<head>
<meta charset="utf-8">
<title>Framewise Build — Business Card</title>
<link rel="stylesheet" href="https://fonts.googleapis.com/css2?family=Montserrat:wght@600&family=Raleway:wght@400;500&family=Nunito+Sans:wght@400&display=swap">
<style>
  :root {
    --page-bg: #eceef0;
    --card-white: #ffffff;
    --card-grey: #d8d9e1;
    --brand-slate: #4a5563;
    --brand-red: #b31e2a;
    --brand-red-dark: #3a0508;
    --ink: #1c1c1c;
  }
  * { margin: 0; padding: 0; box-sizing: border-box; }
  html, body {
    width: 1200px;
    height: 1200px;
    overflow: hidden;
    background: var(--page-bg);
  }
  .canvas {
    position: relative;
    width: 1200px;
    height: 1200px;
  }
  .card {
    position: absolute;
    left: 173px;
    width: 853px;
    height: 487px;
  }
  .card--front { top: 69px; background: var(--card-white); }
  .card--back  { top: 643px; background: var(--card-grey); }

  .brand {
    position: absolute;
    display: flex;
    align-items: center;
    font-family: "Montserrat", sans-serif;
    font-weight: 600;
    color: var(--brand-slate);
    letter-spacing: 1px;
    text-transform: uppercase;
    white-space: nowrap;
  }
  .brand__square {
    width: 40px;
    height: 40px;
    background: var(--brand-red);
    flex: none;
  }
  .card--front .brand {
    left: 64px;
    top: 80px;
    font-size: 30px;
    gap: 24px;
  }
  .card--back .brand {
    left: 0;
    right: 0;
    top: 190px;
    flex-direction: column;
    gap: 42px;
    font-size: 29px;
  }
  .card--back .brand__square { width: 56px; height: 56px; }

  .band {
    position: absolute;
    left: 0;
    top: 168px;
    width: 100%;
    height: 34px;
    background: linear-gradient(to bottom, var(--brand-red-dark) 0%, var(--brand-red) 35%, var(--brand-red) 100%);
  }

  .person {
    position: absolute;
    left: 65px;
    top: 238px;
    font-family: "Raleway", sans-serif;
    color: var(--ink);
  }
  .person__name { font-size: 39px; font-weight: 500; line-height: 1.05; }
  .person__role { font-size: 26px; font-weight: 400; line-height: 1.3; }

  .contact {
    position: absolute;
    left: 70px;
    top: 360px;
    font-family: "Nunito Sans", sans-serif;
    font-size: 25px;
    color: var(--ink);
    line-height: 33px;
    list-style: none;
  }
  .contact__row { display: flex; }
  .contact__label { width: 46px; }
</style>
</head>
<body>
<main class="canvas">
  <section class="card card--front" aria-label="Card front">
    <div class="brand">
      <span class="brand__square" aria-hidden="true"></span>
      <span class="brand__name">Framewise Build</span>
    </div>
    <div class="band"></div>
    <div class="person">
      <h1 class="person__name">Marcus Helby</h1>
      <p class="person__role">Director</p>
    </div>
    <ul class="contact">
      <li class="contact__row"><span class="contact__label">M:</span><span>0427 593184</span></li>
      <li class="contact__row"><span class="contact__label">E:</span><span>marcus@framewisebuild.com.au</span></li>
      <li class="contact__row"><span class="contact__label">W</span><span>www.framewisebuild.com.au</span></li>
    </ul>
  </section>

  <section class="card card--back" aria-label="Card back">
    <div class="brand">
      <span class="brand__square" aria-hidden="true"></span>
      <span class="brand__name">Framewise Build</span>
    </div>
  </section>
</main>
</body>
</html>
```